" consultorio medico com dermatologistas e cirurgião vascular que realiza tratamentos estéticos, capilares e prevenção/diagnostico e tratamento do cancer de pele baseado em lasers e tecnologias "

```html
<!DOCTYPE html>
<html lang="pt-BR">
<head>
<meta charset="UTF-8">
<title>Solvie Clínica – Papelaria</title>
<link rel="stylesheet" href="https://fonts.googleapis.com/css2?family=Montserrat:wght@500&display=swap">
<style>
  :root {
    --stage: #ecebe8;
    --paper: #ffffff;
    --navy: #0f1726;
    --gold: #c9a35a;
    --silver: #c9ccd1;
    --rule: #2a2a2a;
  }
  * { box-sizing: border-box; margin: 0; padding: 0; }
  html, body {
    width: 1200px;
    height: 1200px;
    overflow: hidden;
    background: var(--stage);
  }
  .stationery {
    position: relative;
    width: 1200px;
    height: 1200px;
  }
  .envelope {
    position: absolute;
    left: 44px;
    top: 212px;
    width: 526px;
    height: 772px;
    background: var(--paper);
    box-shadow: 0 4px 14px rgba(0,0,0,0.18);
  }
  .envelope-flap {
    position: absolute;
    left: 0;
    top: 0;
    width: 526px;
    height: 74px;
  }
  .envelope-brand {
    position: absolute;
    left: 0;
    right: 0;
    top: 668px;
    text-align: center;
    font-family: "Montserrat", sans-serif;
    font-weight: 500;
    font-size: 15px;
    letter-spacing: 2px;
    text-transform: uppercase;
    color: var(--gold);
  }
  .envelope-address {
    position: absolute;
    left: 148px;
    top: 712px;
    width: 230px;
  }
  .folder {
    position: absolute;
    left: 635px;
    top: 210px;
    width: 530px;
    height: 774px;
    background: var(--navy);
    box-shadow: 0 4px 14px rgba(0,0,0,0.25);
  }
  .folder-brand {
    position: absolute;
    left: 0;
    right: 0;
    top: 166px;
    text-align: center;
    font-family: "Montserrat", sans-serif;
    font-weight: 500;
    font-size: 28px;
    letter-spacing: 4px;
    text-transform: uppercase;
    color: var(--gold);
  }
  .folder-bands {
    position: absolute;
    left: 0;
    bottom: 0;
    width: 530px;
    height: 10px;
  }
</style>
</head>
<body>
<main class="stationery">

  <section class="envelope" aria-label="Envelope">
    <svg class="envelope-flap" viewBox="0 0 526 74" aria-hidden="true">
      <polygon points="0,0 526,0 526,8 512,74 14,74 0,8" fill="var(--navy)"/>
    </svg>
    <p class="envelope-brand">Solvie Clínica</p>
    <svg class="envelope-address" viewBox="0 0 230 24" aria-hidden="true">
      <circle cx="3" cy="6" r="2.5" fill="var(--rule)"/>
      <line x1="12" y1="6" x2="230" y2="6" stroke="var(--rule)" stroke-width="2"/>
      <line x1="12" y1="20" x2="200" y2="20" stroke="var(--rule)" stroke-width="2"/>
    </svg>
  </section>

  <section class="folder" aria-label="Pasta">
    <p class="folder-brand">Solvie Clínica</p>
    <svg class="folder-bands" viewBox="0 0 530 10" aria-hidden="true">
      <rect x="0" y="0" width="180" height="10" fill="var(--gold)"/>
      <rect x="192" y="0" width="72" height="10" fill="var(--silver)"/>
    </svg>
  </section>

</main>
</body>
</html>
```